I would like to modify/update my 2 step login screen

I want a more modern looking login page for our document imaging application. I need to keep all of the same elements and buttons that currently exist. The first 2 screens are the login. The 3rd is a screenshot of the actual application home page.

```html
<!DOCTYPE html>
<html lang="en">
<head>
<meta charset="utf-8">
<title>MSS Login</title>
<link href="https://fonts.googleapis.com/css2?family=Poppins:wght@400;500;600;700&family=Lato:wght@400;700&display=swap" rel="stylesheet">
<style>
  :root {
    --page-bg: #efefef;
    --card-bg: #ffffff;
    --brand-red: #8b0c06;
    --brand-gold: #8a7a3a;
    --ink: #111111;
    --muted: #8a8a8a;
    --line: #d9d9d9;
    --focus: #2f8fd8;
    --button-border: #b9b9c4;
  }
  * { box-sizing: border-box; margin: 0; padding: 0; }
  html, body { width: 1079px; height: 1200px; overflow: hidden; }
  body { background: var(--page-bg); font-family: "Poppins", sans-serif; color: var(--ink); position: relative; }

  .login-screen {
    position: absolute; left: 30px; top: 305px; width: 1019px; height: 590px;
    background: var(--card-bg); box-shadow: 0 6px 24px rgba(0,0,0,.12);
  }
  .abs { position: absolute; }

  .brand { left: 70px; top: 58px; display: flex; align-items: center; gap: 8px; }
  .brand-mark { width: 18px; height: 18px; background: var(--brand-red); }
  .brand-name { font-weight: 600; font-size: 15px; color: var(--brand-red); letter-spacing: .5px; }

  .product-hub {
    left: 270px; top: 206px; width: 94px; height: 94px; border-radius: 50%;
    border: 2px solid var(--brand-red); display: flex; align-items: center; justify-content: center;
    font-weight: 700; font-size: 15px; color: var(--brand-red);
  }

  .feature {
    background: #fff; border-radius: 18px; box-shadow: 3px 4px 10px rgba(0,0,0,.12);
    padding: 6px 14px 6px 10px; font-weight: 700; font-size: 9px; line-height: 1.1; color: var(--brand-red);
  }

  .stat-tile {
    left: 173px; top: 406px; width: 95px; height: 95px; border-radius: 10px; background: var(--brand-red);
    color: #fff; padding: 14px 10px;
  }
  .stat-value { font-weight: 400; font-size: 30px; line-height: 1; }
  .stat-label { font-weight: 600; font-size: 11px; margin-top: 6px; }

  .members-pill {
    left: 290px; top: 423px; width: 220px; height: 52px; border-radius: 12px; background: var(--brand-red);
    color: #fff; display: flex; align-items: center; padding: 0 8px;
  }
  .avatars { display: flex; }
  .avatar { width: 30px; height: 30px; border-radius: 50%; background: #ece8e2; border: 2px solid #fff; margin-right: -8px; }
  .members-text { margin-left: 20px; }
  .members-count { font-size: 8px; }
  .members-note { font-size: 7px; font-weight: 600; margin-top: 4px; }

  .login-form { left: 648px; top: 104px; width: 258px; }
  .welcome { font-size: 8px; font-weight: 500; }
  .title { font-size: 18px; font-weight: 500; margin-top: 2px; }
  .field-label { font-size: 9px; font-weight: 500; margin-top: 18px; }
  .field-input { margin-top: 6px; height: 28px; border: 2px solid var(--focus); border-radius: 5px; position: relative; }
  .field-input::before { content: ""; position: absolute; left: 8px; top: 5px; width: 1px; height: 14px; background: #555; }
  .primary-button {
    margin-top: 19px; height: 36px; border-radius: 5px; background: var(--brand-red); color: #fff;
    font-size: 10px; font-weight: 500; display: flex; align-items: center; justify-content: center;
  }
  .divider { margin-top: 24px; display: flex; align-items: center; gap: 22px; color: var(--muted); font-size: 9px; font-family: "Lato", sans-serif; }
  .divider::before, .divider::after { content: ""; flex: 1; height: 1px; background: var(--line); }
  .sso-button {
    margin-top: 10px; height: 28px; border: 1px solid var(--button-border); border-radius: 5px;
    display: flex; align-items: center; justify-content: center; gap: 8px;
    font-family: "Lato", sans-serif; font-size: 10px; color: #444;
  }
  .sso-button:first-of-type { margin-top: 18px; }
  .sso-icon { width: 9px; height: 9px; background: #222; }
  .sso-icon.round { border-radius: 50%; }
  .notice { margin-top: 25px; text-align: center; font-size: 5.5px; line-height: 1.8; color: #444; }
  .footer-links { left: 648px; top: 538px; width: 258px; display: flex; justify-content: space-around; font-size: 5.5px; color: var(--muted); text-decoration: underline; }
</style>
</head>
<body>
  <main class="login-screen">
    <div class="abs brand"><span class="brand-mark"></span><span class="brand-name">MERIDIAN SYSTEMS</span></div>

    <div class="abs product-hub">DocuView</div>
    <div class="abs feature" style="left:192px;top:177px;">Document<br>Archive</div>
    <div class="abs feature" style="left:374px;top:177px;">HR<br>Onboarding</div>
    <div class="abs feature" style="left:166px;top:236px;">Electronic<br>Forms &amp;<br>Workflows</div>
    <div class="abs feature" style="left:406px;top:248px;padding:8px 16px;">eSigning</div>
    <div class="abs feature" style="left:192px;top:299px;">Mileage &amp;<br>Expense<br>Tracking</div>
    <div class="abs feature" style="left:372px;top:299px;">Scanning &amp;<br>Database<br>Conversion</div>

    <div class="abs stat-tile">
      <div class="stat-value">25+</div>
      <div class="stat-label">Companies</div>
    </div>
    <div class="abs members-pill">
      <div class="avatars" role="img" aria-label="Member portraits">
        <span class="avatar"></span><span class="avatar"></span><span class="avatar"></span>
      </div>
      <div class="members-text">
        <div class="members-count">+ 5K members</div>
        <div class="members-note">Trust our premium solutions</div>
      </div>
    </div>

    <section class="abs login-form">
      <div class="welcome">Welcome!</div>
      <h1 class="title">MSS Login</h1>
      <div class="field-label">Databese</div>
      <div class="field-input"></div>
      <div class="primary-button">Log in with MyDocuView</div>
      <div class="divider">OR</div>
      <div class="sso-button"><span class="sso-icon round"></span>Log in with Nimbus</div>
      <div class="sso-button"><span class="sso-icon"></span>Log in with Vertex</div>
      <div class="sso-button"><span class="sso-icon round"></span>Log in with KeyPass</div>
      <p class="notice">All activity on this site is being recorded.<br>Your IP Address is being saved as '192.168.168.134'</p>
    </section>

    <nav class="abs footer-links"><span>Privacy</span><span>Remote Support</span><span>Contact Us</span></nav>
  </main>
</body>
</html>
```